Website design for a construction company

The logo and the copies of all the 3 pages are attached below. I don't have a preference in colors but I would ideally like to use the colors on my logo, dark teal (secondary) and copper (primary).

Company Name: Torvin Group

Location: London, UK

Business Overview:

Torvin Group is a comprehensive construction company based in London, specializing in a wide range of construction services. We cater to various sectors, providing services including electrical work, painting and decorating, plastering, plumbing, carpentry, kitchen and bathroom installations, loft conversions, and extensions. Our team is known for its skilled craftsmanship, attention to detail, and commitment to quality.

What "TORVIN" stands for:

Our company name, 'TORVIN', is derived from Hephaestus, the ancient Greek god of craftsmen, blacksmiths, artisans, sculptors, metals, metallurgy, fire, and volcanoes. Hephaestus was renowned in mythology for his incredible skill in crafting and creating, making him the patron of all craftsmen and artisans. His name is synonymous with the mastery of artisanship and the creation of wondrous, enduring works.

In choosing 'TORVIN' as our name, we embody the spirit and skills of Hephaestus. It reflects our commitment to craftsmanship, excellence, and durability in the field of construction. Just as Hephaestus was known for his meticulous work, precision, and innovative creations, our company strives to uphold these qualities in every project we undertake.

Our name is a constant reminder of our dedication to quality, innovation, and the art of building. It symbolizes our endeavor to achieve the highest standards in construction, much like Hephaestus did in his timeless creations. In essence, 'TORVIN' is not just our name; it's a representation of our ethos and the high standards we set for ourselves in the construction industry.

Target Audience:

Our primary audience includes homeowners, real estate developers, and commercial clients in London seeking reliable, high-quality construction services.

Unique Selling Points:

Diverse Range of Services: Offering a one-stop solution for all construction needs.

Certified and Experienced: Professional team with a strong focus on delivering certified and compliant work, particularly in electrical services.

Client-Centric Approach: Emphasizing client satisfaction, we tailor our services to meet the unique needs and visions of our clients.

Quality and Reliability: Commitment to high-quality materials, skilled workmanship, and delivering projects on time and within budget.

Website Requirements:

Clean, professional design reflecting the quality and reliability of our services.

User-friendly navigation to easily access information about our services, portfolio, company background, and contact details.

Portfolio section showcasing our past projects with placeholders for images and descriptions.

Integration of a contact form, map for our location, and links to our social media accounts.

Mobile-responsive design to ensure accessibility across various devices.

Purpose of the Website:
The website aims to:

Establish an online presence and credibility in the construction industry.

Provide an informative resource about our services and past projects to potential clients.

Facilitate easy communication and inquiries through an integrated contact system.

Tone and Style:

Professional, informative, and welcoming. The website should convey trustworthiness and expertise in the construction field.

homeowners, real estate developers, and commercial clients

Construction

3 page

```html
<!DOCTYPE html>
<html lang="en">
<head>
<meta charset="utf-8">
<title>Torvin Group – Construction in London</title>
<link href="https://fonts.googleapis.com/css2?family=Inter:ital,wght@0,400;0,500;0,600;0,700;1,400;1,500&display=swap" rel="stylesheet">
<style>
:root{
  --teal:#16918a;
  --teal-dark:#0f7c75;
  --copper:#b5853f;
  --copper-light:#c99a57;
  --ink:#151515;
  --text:#555;
  --white:#fff;
  --black:#131313;
}
*{margin:0;padding:0;box-sizing:border-box}
html,body{width:1200px;height:3504px;overflow:hidden}
body{font-family:'Inter',sans-serif;color:var(--ink);background:var(--white)}
.page{position:relative;width:1200px;height:3504px;overflow:hidden}
.abs{position:absolute}
.band{position:absolute;left:0;width:1200px}
.shapes{position:absolute;left:0;top:0}

.topbar{left:664px;top:0;width:390px;height:30px;background:var(--teal);color:#fff;font-size:14px;display:flex;align-items:center;justify-content:space-around;clip-path:polygon(0 0,100% 0,95% 100%,5% 100%)}
.topbar span{display:flex;align-items:center;gap:6px}
.brand{display:flex;align-items:center;gap:8px;font-weight:500;font-size:22px;color:var(--ink);white-space:nowrap;line-height:1}
.brand .mark{width:28px;height:28px;background:var(--copper);flex:none}
.brand.footer-brand{font-size:24px;color:#fff}
.brand.footer-brand .mark{width:32px;height:32px}
.nav{left:370px;top:57px;display:flex;gap:32px;font-size:14px;font-weight:500}
.btn{display:inline-flex;align-items:center;gap:8px;border-radius:40px;color:#fff;font-weight:600;position:absolute;justify-content:center}
.btn.teal{background:var(--teal)}
.btn.copper{background:var(--copper)}
.btn svg{width:14px;height:14px}

.hero-img{left:0;top:101px;width:1200px;height:552px;background:linear-gradient(100deg,#e7e1d8 0%,#f4f1ec 35%,#ece6dc 60%,#d9d0c2 100%)}
.hero-title{left:144px;top:240px;font-size:38px;font-weight:600;line-height:52px;letter-spacing:.3px}
.hero-title em{font-style:normal;color:var(--copper)}
.hero-sub{left:144px;top:362px;font-size:17px;font-weight:500;line-height:26px}

.h2{position:absolute;font-weight:600;text-align:center;width:1200px;left:0}
.h2.light{color:#fff}
.rule{position:absolute;height:3px;background:#fff;width:82px}
.rule.teal{background:var(--teal);width:120px}

.feature{position:absolute;width:310px;text-align:center;color:#fff}
.feature .icon{width:114px;height:114px;border-radius:50%;background:var(--copper);border:8px solid rgba(201,154,87,.45);background-clip:padding-box;margin:0 auto;display:flex;align-items:center;justify-content:center;box-shadow:0 0 0 8px rgba(201,154,87,.35)}
.feature h3{font-size:17px;font-weight:600;margin-top:40px}
.feature p{font-size:13px;line-height:23px;margin-top:14px}

.welcome-title{left:145px;top:1302px;font-size:33px;font-weight:700}
.welcome-title span{color:var(--copper)}
.welcome-copy{left:145px;top:1383px;width:408px;font-size:13px;line-height:24px;color:var(--text);text-align:justify}
.welcome-copy p+p{margin-top:8px}
.welcome-img{left:678px;top:1257px;width:379px;height:358px;background:linear-gradient(135deg,var(--teal) 0%,#5aa9a0 30%,var(--copper-light) 60%,var(--copper) 100%)}

.services-sub{left:140px;top:1872px;width:920px;text-align:center;color:#fff;font-size:18px;line-height:29px}
.card{position:absolute;top:1973px;width:287px;height:415px;background:#fff;border-radius:10px;box-shadow:0 6px 18px rgba(0,0,0,.12);text-align:center}
.card .photo{margin:7px;height:199px;border-radius:6px}
.card .badge{position:absolute;left:110px;top:172px;width:66px;height:66px;border-radius:50%;background:var(--teal);border:3px solid #fff;display:flex;align-items:center;justify-content:center}
.card h3{margin-top:44px;font-size:18px;font-weight:600}
.card p{margin:10px 14px 0;font-size:12.5px;line-height:21px;color:var(--text)}
.card .btn{left:70px;top:360px;width:148px;height:38px;font-size:14px}
.dots{left:578px;top:2427px;display:flex;gap:6px}
.dots i{width:11px;height:11px;border-radius:50%;background:#d5d5d5;display:block}
.dots i.on{background:var(--teal)}

.contact-title{left:144px;top:2515px;font-size:33px;font-weight:700}
.contact-title span{color:var(--copper)}
.contact-copy{left:144px;top:2600px;width:900px;font-size:18px;line-height:30px;font-style:italic;color:#444}

.avatar{left:214px;top:2917px;width:84px;height:84px;background:linear-gradient(135deg,#9fd3e6,#dceff5);transform:rotate(45deg);border-radius:8px}
.quote{left:342px;top:2920px;width:580px;color:#fff;font-size:13.5px;line-height:25px;font-style:italic}
.client{left:342px;top:3006px;color:#fff;font-weight:600;font-size:16px}
.company{left:342px;top:3033px;color:#fff;font-size:11px}

.footer-h{position:absolute;top:3174px;color:#fff;font-weight:600;font-size:16px}
.links{left:409px;top:3230px;list-style:none;color:#fff;font-size:13px;line-height:26px}
.info{left:599px;top:3232px;color:#fff;font-size:13px;list-style:none}
.info li{display:flex;gap:10px;align-items:flex-start;line-height:18px;margin-bottom:11px}
.info svg{width:14px;height:14px;flex:none;margin-top:2px}
.field{position:absolute;left:865px;width:191px;background:#fff;border-radius:4px;font-size:9px;color:#999;padding:6px 7px}
.social{position:absolute;top:3303px;width:34px;height:34px;border-radius:50%;background:#fff}
.divider{left:144px;top:3435px;width:912px;height:1px;background:#444}
.copy{left:0;top:3461px;width:1200px;text-align:center;color:#fff;font-size:11px}
</style>
</head>
<body>
<div class="page">

  <div class="band" style="top:600px;height:700px;background:var(--teal)"></div>
  <div class="band" style="top:1600px;height:578px;background:var(--copper)"></div>
  <div class="band" style="top:2500px;height:700px;background:var(--teal)"></div>

  <div class="abs hero-img" role="img" aria-label="Bright white kitchen with marble walls and brass pendant lights"></div>

  <svg class="shapes" width="1200" height="3504" viewBox="0 0 1200 3504" aria-hidden="true">
    <path d="M1200,450 Q1200,653 860,653 L1200,653 Z" fill="var(--teal)"/>
    <path d="M0,1330 Q0,1184 180,1184 L1200,1184 L1200,1510 Q1200,1707 1000,1707 L0,1707 Z" fill="#fff"/>
    <path d="M0,2178 L1200,2178 L1200,2520 Q1200,2785 900,2785 L0,2785 Z" fill="#fff"/>
    <path d="M0,3250 Q0,3099 180,3099 L1200,3099 L1200,3504 L0,3504 Z" fill="var(--black)"/>
  </svg>

  <div class="abs" style="left:0;top:0;width:1200px;height:101px;background:#fff"></div>
  <div class="abs topbar">
    <span><svg width="12" height="12" viewBox="0 0 24 24" fill="#fff"><path d="M6.6 10.8a15 15 0 006.6 6.6l2.2-2.2c.3-.3.7-.4 1-.2 1.1.4 2.3.6 3.6.6.6 0 1 .4 1 1V20c0 .6-.4 1-1 1A17 17 0 013 4c0-.6.4-1 1-1h3.5c.6 0 1 .4 1 1 0 1.3.2 2.5.6 3.6.1.3 0 .7-.2 1z"/></svg>888-888-8888</span>
    <span><svg width="13" height="11" viewBox="0 0 24 18" fill="#fff"><path d="M0 0h24v2L12 10 0 2zM0 4l12 8 12-8v14H0z"/></svg>info@torvingroup.com</span>
  </div>
  <div class="abs brand" style="left:144px;top:38px"><span class="mark"></span>TORVIN GROUP</div>
  <nav class="abs nav"><span>Home</span><span>About Us</span><span>Why Choose Us</span><span>Our Services</span><span>Contact Us</span></nav>
  <span class="btn teal" style="left:897px;top:47px;width:158px;height:39px;font-size:15px">Request Quote</span>

  <h1 class="abs hero-title"><em>BUILDING</em> YOUR<br>DREAMS INTO <em>REALITY</em></h1>
  <p class="abs hero-sub">Expert Craftsmanship Meets Unmatched Reliability in the<br>Heart of London Introduction Section.</p>
  <span class="btn teal" style="left:144px;top:439px;width:191px;height:49px;font-size:17px">Call To Action <svg viewBox="0 0 16 16"><circle cx="8" cy="8" r="8" fill="#fff"/><path d="M6.5 4.5L10 8l-3.5 3.5" stroke="var(--teal)" stroke-width="2" fill="none"/></svg></span>

  <h2 class="h2 light" style="top:730px;font-size:33px">WHY CHOOSE US</h2>
  <div class="rule" style="left:540px;top:783px;width:120px"></div>

  <div class="feature" style="left:117px;top:814px">
    <div class="icon"><svg width="56" height="56" viewBox="0 0 56 56" fill="none" stroke="#fff" stroke-width="2.5"><circle cx="24" cy="26" r="9"/><circle cx="24" cy="26" r="16" stroke-dasharray="6 4"/><circle cx="38" cy="38" r="9"/><path d="M34 38l3 3 5-6"/></svg></div>
    <h3>OUR EXPERTISE</h3>
    <p>Leveraging over 10 years of experience, Torvin Group stands as a beacon of excellence in the construction industry.</p>
  </div>
  <span class="btn copper" style="left:204px;top:1082px;width:136px;height:38px;font-size:14px">Learn More <svg viewBox="0 0 16 16"><circle cx="8" cy="8" r="8" fill="#fff"/><path d="M6.5 4.5L10 8l-3.5 3.5" stroke="var(--copper)" stroke-width="2" fill="none"/></svg></span>

  <div class="feature" style="left:448px;top:814px">
    <div class="icon"><svg width="56" height="56" viewBox="0 0 56 56" fill="none" stroke="#fff" stroke-width="2.5"><circle cx="26" cy="22" r="13"/><path d="M20 22l4 4 8-8"/><path d="M18 33l-5 14 7-3 4 6 4-12M34 33l5 14-7-3-4 6"/></svg></div>
    <h3>CERTIFIED EXCELLENCE</h3>
    <p>Our dedication to delivering top-notch results is evident in every project. We use high-quality materials, employ skilled tradespeople.</p>
  </div>
  <span class="btn copper" style="left:535px;top:1082px;width:136px;height:38px;font-size:14px">Learn More <svg viewBox="0 0 16 16"><circle cx="8" cy="8" r="8" fill="#fff"/><path d="M6.5 4.5L10 8l-3.5 3.5" stroke="var(--copper)" stroke-width="2" fill="none"/></svg></span>

  <div class="feature" style="left:778px;top:814px">
    <div class="icon"><svg width="56" height="56" viewBox="0 0 56 56" fill="none" stroke="#fff" stroke-width="2.5"><circle cx="30" cy="18" r="9"/><path d="M26 18l3 3 5-5"/><path d="M8 38h10l8 3h10a3 3 0 000-6h-8M18 38l10-6h10l10-4"/></svg></div>
    <h3>QUALITY ASSURANCE</h3>
    <p>Quality is not just a promise, but a practice. Meticulous attention to detail ensures flawless finishes and durable structures.</p>
  </div>
  <span class="btn copper" style="left:865px;top:1082px;width:136px;height:38px;font-size:14px">Learn More <svg viewBox="0 0 16 16"><circle cx="8" cy="8" r="8" fill="#fff"/><path d="M6.5 4.5L10 8l-3.5 3.5" stroke="var(--copper)" stroke-width="2" fill="none"/></svg></span>

  <h2 class="abs welcome-title"><span>WELCOME</span> MESSAGE</h2>
  <div class="rule teal" style="left:145px;top:1356px"></div>
  <div class="abs welcome-copy">
    <p>Welcome to Torvin Group – Where Construction Meets Excellence. Based in London, we are committed to transforming your spaces into exceptional places.</p>
    <p>Our team is dedicated to delivering the highest quality in every project, attending to every detail with precision and care.</p>
  </div>
  <span class="btn teal" style="left:145px;top:1533px;width:153px;height:41px;font-size:15px">Read More <svg viewBox="0 0 16 16"><circle cx="8" cy="8" r="8" fill="#fff"/><path d="M6.5 4.5L10 8l-3.5 3.5" stroke="var(--teal)" stroke-width="2" fill="none"/></svg></span>
  <div class="abs welcome-img" role="img" aria-label="Collage of tradespeople at work with tools and plans on site"></div>

  <h2 class="h2 light" style="top:1787px;font-size:33px">SERVICES PREVIEW</h2>
  <div class="rule" style="left:540px;top:1840px;width:120px"></div>
  <p class="abs services-sub">Our Services – Tailored to Your Needs. Discover how we can bring your vision to life, covering every aspect of construction from the initial design to the final touches.</p>

  <div class="card" style="left:144px">
    <div class="photo" role="img" aria-label="Electrician wiring a distribution panel" style="background:linear-gradient(135deg,#4a5a68,#9aa3a8)"></div>
    <div class="badge"><svg width="32" height="32" viewBox="0 0 32 32" fill="none" stroke="#fff" stroke-width="2"><path d="M11 19a8 8 0 1110 0v3H11z"/><path d="M12 26h8M13 29h6M16 12v7"/></svg></div>
    <h3>Electrical Work</h3>
    <p>Certified and Safe: Our electrical services encompass everything from installations to repairs and maintenance.</p>
    <span class="btn copper">Read More <svg viewBox="0 0 16 16"><circle cx="8" cy="8" r="8" fill="#fff"/><path d="M6.5 4.5L10 8l-3.5 3.5" stroke="var(--copper)" stroke-width="2" fill="none"/></svg></span>
  </div>
  <div class="card" style="left:458px">
    <div class="photo" role="img" aria-label="Decorator painting a white wall with a roller" style="background:linear-gradient(135deg,#e9e9e9,#c9d3dc)"></div>
    <div class="badge"><svg width="32" height="32" viewBox="0 0 32 32" fill="none" stroke="#fff" stroke-width="2"><rect x="6" y="5" width="18" height="7" rx="1"/><path d="M24 8h3v7H15v4"/><rect x="13" y="19" width="4" height="9"/></svg></div>
    <h3>Painting and Decorating</h3>
    <p>Transforming Spaces: Our painting and decorating services bring new life to your spaces.</p>
    <span class="btn copper">Read More <svg viewBox="0 0 16 16"><circle cx="8" cy="8" r="8" fill="#fff"/><path d="M6.5 4.5L10 8l-3.5 3.5" stroke="var(--copper)" stroke-width="2" fill="none"/></svg></span>
  </div>
  <div class="card" style="left:771px">
    <div class="photo" role="img" aria-label="Plumber fixing pipes under a sink" style="background:linear-gradient(135deg,#2e4d7a,#a9b5c2)"></div>
    <div class="badge"><svg width="32" height="32" viewBox="0 0 32 32" fill="none" stroke="#fff" stroke-width="2"><path d="M20 5a6 6 0 00-5 8L5 23l4 4 10-10a6 6 0 008-5l-4 1-3-3z"/></svg></div>
    <h3>Plumbing</h3>
    <p>Efficient and Reliable: From fixing leaks to installing new systems, our plumbing services are marked by reliability</p>
    <span class="btn copper">Read More <svg viewBox="0 0 16 16"><circle cx="8" cy="8" r="8" fill="#fff"/><path d="M6.5 4.5L10 8l-3.5 3.5" stroke="var(--copper)" stroke-width="2" fill="none"/></svg></span>
  </div>
  <div class="abs dots"><i></i><i class="on"></i><i></i></div>

  <h2 class="abs contact-title"><span>CONTACT</span> US</h2>
  <div class="rule teal" style="left:144px;top:2568px"></div>
  <p class="abs contact-copy">Ready to Start Your Project? Contact us today for a consultation and embark on the journey to turn your construction dreams into a stunning reality.</p>
  <span class="btn teal" style="left:144px;top:2683px;width:148px;height:38px;font-size:14px">Call To Action <svg viewBox="0 0 16 16"><circle cx="8" cy="8" r="8" fill="#fff"/><path d="M6.5 4.5L10 8l-3.5 3.5" stroke="var(--teal)" stroke-width="2" fill="none"/></svg></span>

  <h2 class="abs" style="left:341px;top:2840px;font-size:33px;font-weight:600;color:#fff">TESTIMONIALS</h2>
  <div class="rule" style="left:341px;top:2892px;width:108px"></div>
  <div class="abs avatar" role="img" aria-label="Portrait of a satisfied client"></div>
  <p class="abs quote">Hear from Our Satisfied Clients. Our commitment to excellence has earned us the trust of numerous homeowners and businesses in London. Read their stories and understand the Torvin Group difference</p>
  <p class="abs client">Client Feedback</p>
  <p class="abs company">Company Name</p>

  <div class="abs brand footer-brand" style="left:144px;top:3238px"><span class="mark"></span>TORVIN GROUP</div>
  <span class="social" style="left:167px" aria-label="Social link"></span>
  <span class="social" style="left:206px" aria-label="Social link"></span>
  <span class="social" style="left:246px" aria-label="Social link"></span>
  <span class="social" style="left:285px" aria-label="Social link"></span>

  <h4 class="footer-h" style="left:409px">QUICK LINKS</h4>
  <ul class="abs links"><li>About Us</li><li>Services</li><li>Projects</li><li>Contact Us</li></ul>

  <h4 class="footer-h" style="left:599px">CONTACT INFO</h4>
  <ul class="abs info">
    <li><svg viewBox="0 0 24 24" fill="none" stroke="var(--copper)" stroke-width="2"><path d="M12 22s7-7 7-12a7 7 0 10-14 0c0 5 7 12 7 12z"/><circle cx="12" cy="10" r="2.5"/></svg><span>123, Lorem ipsum dolor sit amet,<br>consectetur adipiscing elit,</span></li>
    <li><svg viewBox="0 0 24 18" fill="none" stroke="var(--copper)" stroke-width="2"><rect x="1" y="1" width="22" height="16"/><path d="M1 1l11 8 11-8"/></svg><span>info@torvinbuild.com</span></li>
    <li><svg viewBox="0 0 24 24" fill="none" stroke="var(--copper)" stroke-width="2"><path d="M6.6 10.8a15 15 0 006.6 6.6l2.2-2.2 5 1.5V21A17 17 0 013 4h4.3l1.5 5z"/></svg><span>+1 888 888 8888</span></li>
    <li><svg viewBox="0 0 24 24" fill="none" stroke="var(--copper)" stroke-width="2"><rect x="3" y="8" width="18" height="13"/><path d="M7 8V3h10v5M7 13h2M11 13h2M15 13h2M7 17h2M11 17h2"/></svg><span>+1 234 567 890</span></li>
  </ul>

  <h4 class="footer-h" style="left:865px">CONNECT</h4>
  <div class="field" style="top:3237px;height:30px">Name*</div>
  <div class="field" style="top:3273px;height:30px">Email*</div>
  <div class="field" style="top:3310px;height:42px">Comment*</div>
  <span class="btn" style="left:865px;top:3362px;width:132px;height:38px;border-radius:3px;background:var(--teal);font-size:15px">Submit Now</span>

  <div class="abs divider"></div>
  <p class="abs copy">© 2024 Torvin Group | All Rights Reserved</p>
</div>
</body>
</html>
```